Step Boldly Toward Gain Promotional Flyer

I Need a one page, one-sided 8.5 x 11 editable promotional flyer that POPS!, designed in photoshop

[TITLE]Step Boldly Toward Gain: 3 BOLD Moves to Up-Level Your Business Now!

[CONTENT for the Flyer:]

At this content-rich event you will learn how to:
• Get out of feast and famine mode and into six, multi-six and/or seven figure-income mode
• Leapfrog your competition and become the obvious choice in your market
• Have your business aligned with who you are and what you want
• Enjoy your business far more than you imagined possible.
• Have more fun and time to yourself
• Live free and unbound!

Accolades
“Delphine helped us increase our six figure income by 41%...I feel reborn!” Marlene & Otis Pruitt, Vienna, VA

“…Delphine is a joy to listen to - compelling, smart, provocative…” – Dennis Ashcombe, Charlotte, North Carolina

“Delphine helped me increase my business by 66%...without me spending more time, money, or making cold calls! …I am in the zone!” Tina Worsley, Baltimore, MD
“Delphine is an energetic and dynamic speaker…content-rich…holds your attention to the very end!” Neil Barrow, Frmr Pres., Crane & Whitby, MD, MD, D.C., PA, DE, NJ
“Delphine is the real estate whisperer!” Hal Drummond, Washington D.C.

“Delphine was prepared, funny, informative and made a connection with each of our agents…Fabulous!…even my admins were PUMPED!!! – Paul Venable, New York

About Delphine:
Delphine is a highly regarded business development speaker & coach who knows how to pump up an audience and have them making more money, in less time, AND having more fun doing it! What’s not to love?! Consistently rated as an exceptional speaker and conference favorite! Among her work: Standout Method: How to Draw Your Best Buyers Time after Time!, Contact Sourcing Done Easy, The Worst Outreach Errors Real Estate Agents Commit and How to Steer Clear of Them, Slow Seasons Build Sharp Sellers, Drive Within the Head for Real Estate Agents.

[Also need a section for:]
Date: December 9, 2015, Time: 9:00 Am - 12:00 Noon, Place: Harbor Lantern Convention, Green Castle, PA

Target Market(s)

Real Estate Agents

Industry/Entity Type

Real Estate Agent

Font styles to use
Sans Serif

Colors
0655a3
f37122

Requirements
Must have
• the peak tier realty mentor logo
Nice to have
• step boldly toward gain logo; lots of POP! :-) ; open to other colors, accent colors.

```html
<!DOCTYPE html>
<html lang="en">
<head>
<meta charset="utf-8">
<title>Step Boldly Toward Gain – Event Flyer</title>
<link href="https://fonts.googleapis.com/css2?family=Source+Sans+3:wght@400;600&display=swap" rel="stylesheet">
<style>
  :root {
    --navy: #0b0d5c;
    --orange: #e97c28;
    --white: #ffffff;
    --page: #e6eaeb;
    --photo-light: #e9e7e4;
    --photo-dark: #6b5a48;
  }
  * { margin: 0; padding: 0; box-sizing: border-box; }
  html, body { width: 1200px; height: 960px; overflow: hidden; background: var(--page); }
  body { font-family: "Source Sans 3", sans-serif; color: var(--white); }
  .flyer {
    position: absolute; left: 270px; top: 13px;
    width: 660px; height: 934px;
    background: var(--navy); overflow: hidden;
  }
  .flyer-title {
    position: absolute; left: 31px; top: 34px;
    font-size: 19.5px; font-weight: 600; color: var(--orange); letter-spacing: -0.2px;
    white-space: nowrap;
  }
  .intro { position: absolute; left: 23px; top: 70px; font-size: 12.3px; line-height: 17px; letter-spacing: -0.2px; }
  .intro ul { list-style: none; }
  .intro li::before { content: "• "; }
  .section-heading { font-size: 21px; font-weight: 600; color: var(--orange); letter-spacing: -0.2px; }
  .accolades { position: absolute; left: 21px; top: 203px; width: 590px; }
  .accolades .section-heading { margin-bottom: 10px; }
  .quote { font-size: 12.3px; line-height: 17px; letter-spacing: -0.25px; }
  .quote.spaced { margin-bottom: 17px; }
  .speaker-photo {
    position: absolute; left: 21px; top: 498px; width: 166px; height: 201px;
    border: 2px solid var(--orange);
    background: linear-gradient(180deg, var(--photo-light) 0%, var(--photo-light) 45%, var(--photo-dark) 100%);
  }
  .about { position: absolute; left: 205px; top: 512px; width: 425px; }
  .about p { font-size: 12.3px; line-height: 17px; letter-spacing: -0.25px; margin-top: 3px; }
  .wave { position: absolute; left: 0; top: 0; }
  .event { position: absolute; left: 340px; top: 736px; width: 310px; text-align: center; white-space: nowrap; }
  .event-date { font-size: 27px; line-height: 34px; font-weight: 600; color: var(--orange); margin-left: 24px; }
  .event-line { font-size: 15.5px; line-height: 20px; letter-spacing: -0.2px; }
  .brand { position: absolute; left: 27px; top: 838px; font-size: 24px; font-weight: 400; color: var(--white); }
</style>
</head>
<body>
  <main class="flyer">
    <svg class="wave" width="660" height="934" viewBox="0 0 660 934" aria-hidden="true">
      <path d="M151 726 C 300 770 400 890 540 905 C 590 910 630 905 660 898 L 660 934 L 151 934 Z" fill="var(--orange)"/>
      <path d="M151 726 C 280 790 370 880 490 934 L 0 934 L 0 726 Z" fill="var(--navy)"/>
      <path d="M0 748 C 90 722 200 765 280 823 C 360 880 410 915 457 934 L 0 934 Z" fill="var(--orange)"/>
    </svg>

    <h1 class="flyer-title">Step Boldly Toward Gain: 3 BOLD Moves to Up-Level Your Business Now!</h1>

    <section class="intro">
      <p>At this content-rich event you will learn how to:</p>
      <ul>
        <li>Get out of feast and famine mode and into six, multi-six and/or seven figure-income mode</li>
        <li>Leapfrog your competition and become the obvious choice in your market</li>
        <li>Have your business aligned with who you are and what you want</li>
        <li>Enjoy your business far more than you imagined possible.</li>
        <li>Have more fun and time to yourself</li>
        <li>Live free and unbound!</li>
      </ul>
    </section>

    <section class="accolades">
      <h2 class="section-heading">Accolades</h2>
      <p class="quote spaced">“Delphine helped us increase our six figure income by 41%...I feel reborn!” Marlene &amp; Otis Pruitt, Vienna, VA</p>
      <p class="quote spaced">“…Delphine is a joy to listen to - compelling, smart, provocative…” – Dennis Ashcombe, Charlotte, North Carolina</p>
      <p class="quote">“Delphine helped me increase my business by 66%...without me spending more time, money, or making cold calls! …I am in the zone!” Tina Worsley, Baltimore, MD</p>
      <p class="quote spaced">“Delphine is an energetic and dynamic speaker…content-rich…holds your attention to the very end!” Neil Barrow, Frmr</p>
      <p class="quote">Pres., Crane &amp; Whitby, MD, MD, D.C., PA, DE, NJ</p>
      <p class="quote spaced">“Delphine is the real estate whisperer!” Hal Drummond, Washington D.C.</p>
      <p class="quote">“Delphine was prepared, funny, informative and made a connection with each of our agents…Fabulous!…even my admins were PUMPED!!! – Paul Venable, New York</p>
    </section>

    <div class="speaker-photo" role="img" aria-label="Portrait photo of speaker Delphine"></div>

    <section class="about">
      <h2 class="section-heading">About Delphine</h2>
      <p>Delphine is a highly regarded business development speaker &amp; coach who knows how to pump up an audience and have them making more money, in less time, AND having more fun doing it! What’s not to love?! Consistently rated as an exceptional speaker and conference favorite! Among her work: Standout Method: How to Draw Your Best Buyers Time after Time!, Contact Sourcing Done Easy, The Worst Outreach Errors Real Estate Agents Commit and How to Steer Clear of Them, Slow Seasons Build Sharp Sellers, Drive Within the Head for Real Estate Agents.</p>
    </section>

    <section class="event">
      <p class="event-date">December 9, 2015</p>
      <p class="event-line">9:00 Am - 12:00 Noon</p>
      <p class="event-line">at</p>
      <p class="event-line">Harbor Lantern Convention, Green Castle, PA</p>
    </section>

    <p class="brand">Step Boldly Toward Gain</p>
  </main>
</body>
</html>
```